Alaska Wedding Cruise Design for Social Media, Print, and Sweatshirts

We are getting married on the Coral Voyager during a cruise to Alaska. We would like a design based on The Harbor Hearts that includes the information below. Ideally, we want the design to be similar to The Harbor Hearts Revisited splash image attached, but the background changed to Alaska scenery, i.e., mountains, a glacier, and northern lights (see IMG_4185), and the logo updated to the original The Harbor Hearts logo. This design will be used in social media group splash headers, printed documents for the wedding, and on sweatshirts.
Tom and Derek Tie the Knot
May 25, 2025
Coral Voyager

```html
<!DOCTYPE html>
<html lang="en">
<head>
<meta charset="utf-8">
<title>Tom and Derek Tie the Knot</title>
<link href="https://fonts.googleapis.com/css2?family=Playfair+Display+SC:wght@400;700&display=swap" rel="stylesheet">
<style>
  :root {
    --sky-top: #ffffff;
    --sky-bottom: #e4f2fb;
    --ink: #0d62a6;
    --wave-1: #d8edf9;
    --wave-2: #a9dbf2;
    --wave-3: #6ec5ec;
    --wave-4: #3cb0e4;
    --sea: #29a8e0;
    --art-top: #dde9f4;
    --art-mid: #b9d2e4;
    --art-bottom: #a6d6e2;
  }
  html, body { margin: 0; padding: 0; overflow: hidden; }
  .canvas {
    position: relative;
    width: 1200px;
    height: 1200px;
    overflow: hidden;
    background: linear-gradient(to bottom, var(--sky-top) 0%, var(--sky-bottom) 75%);
    font-family: "Playfair Display SC", Georgia, serif;
    color: var(--ink);
  }
  .hero-art {
    position: absolute;
    left: 367px;
    top: 111px;
    width: 466px;
    height: 433px;
  }
  .headline {
    position: absolute;
    top: 600px;
    left: 0;
    width: 100%;
    margin: 0;
    text-align: center;
    font-weight: 700;
    font-size: 54px;
    line-height: 64px;
    letter-spacing: 0.5px;
  }
  .event-date {
    position: absolute;
    top: 772px;
    left: 0;
    width: 100%;
    margin: 0;
    text-align: center;
    font-weight: 400;
    font-size: 34px;
    line-height: 40px;
  }
  .event-venue {
    position: absolute;
    top: 812px;
    left: 0;
    width: 100%;
    margin: 0;
    text-align: center;
    font-weight: 700;
    font-size: 32px;
    line-height: 40px;
  }
  .sea {
    position: absolute;
    left: 0;
    bottom: 0;
    width: 1200px;
    height: 310px;
  }
</style>
</head>
<body>
<main class="canvas">
  <svg class="hero-art" viewBox="0 0 466 433" role="img" aria-label="Heart-shaped illustration of snowy Alaskan mountains and a glacier with falling snow, with a cruise ship sailing below">
    <defs>
      <linearGradient id="heroFill" x1="0" y1="0" x2="0" y2="1">
        <stop offset="0" stop-color="var(--art-top)"/>
        <stop offset="0.6" stop-color="var(--art-mid)"/>
        <stop offset="1" stop-color="var(--art-bottom)"/>
      </linearGradient>
    </defs>
    <path fill="url(#heroFill)" d="M233 433 L28 230 C-10 190 -8 100 40 50 C95 -5 190 0 233 60 C276 0 371 -5 426 50 C474 100 476 190 438 230 Z"/>
  </svg>

  <h1 class="headline">Tom and Derek<br>Tie the Knot</h1>
  <p class="event-date">May 25, 2025</p>
  <p class="event-venue">Coral Voyager</p>

  <svg class="sea" viewBox="0 0 1200 310" preserveAspectRatio="none" aria-hidden="true">
    <path fill="var(--wave-1)" d="M0 20 C150 0 300 30 450 14 C600 0 750 28 900 12 C1020 2 1120 18 1200 14 L1200 310 L0 310 Z"/>
    <path fill="var(--wave-2)" d="M0 48 C120 30 260 58 400 42 C540 26 680 56 820 40 C960 24 1080 52 1200 38 L1200 310 L0 310 Z"/>
    <path fill="var(--wave-3)" d="M0 76 C140 58 280 88 420 70 C560 54 700 84 840 68 C980 52 1100 80 1200 66 L1200 310 L0 310 Z"/>
    <path fill="var(--wave-4)" d="M0 100 C150 84 300 112 450 96 C600 80 750 108 900 92 C1020 82 1120 100 1200 92 L1200 310 L0 310 Z"/>
    <path fill="var(--sea)" d="M0 124 C150 110 300 134 450 120 C600 106 750 132 900 118 C1020 108 1120 124 1200 118 L1200 310 L0 310 Z"/>
  </svg>
</main>
</body>
</html>
```